School Poster

Design so that these can be placed in classrooms across the school.

Attached is another design we have had done. Use a similar theme.

Consider using themes from https://tolvanehs.qx.edu.au/

please edit Binder1 doc.

Target Market(s)

Students and teachers

```html
<!DOCTYPE html>
<html lang="en">
<head>
<meta charset="utf-8">
<title>Classroom Posters – Tolvane SHS</title>
<link href="https://fonts.googleapis.com/css2?family=Poppins:wght@300;400;500;600;700;800;900&display=swap" rel="stylesheet">
<style>
:root{
  --navy:#2f3f96;
  --navy-deep:#26357f;
  --yellow:#f3ea7b;
  --yellow-bright:#f6e54a;
  --panel:#ffffff;
  --soft:#ededee;
  --ink:#24306f;
  --text:#2c2c33;
  --red:#d3292e;
  --stage:#e8e9e8;
}
*{box-sizing:border-box;margin:0;padding:0}
html,body{width:1200px;height:960px;overflow:hidden;background:var(--stage);font-family:"Poppins",sans-serif}
.canvas{position:relative;width:1200px;height:960px}
.poster{position:absolute;top:144px;width:476px;height:672px;background:var(--navy);overflow:hidden}
.poster--steps{left:106px}
.poster--ai{left:618px}
.header{position:absolute;left:0;top:0;width:100%;height:101px;background:radial-gradient(ellipse at 70% 40%,#3a4ca6 0%,var(--navy-deep) 75%)}
.title{position:absolute;left:24px;top:19px;font-weight:800;font-size:33px;line-height:33px;color:#fff;letter-spacing:.2px}
.title .accent{color:var(--yellow-bright)}
.school-name{position:absolute;right:24px;top:30px;width:60px;color:#fff;font-weight:700;font-size:12px;line-height:15px;text-align:center;display:flex;flex-direction:column;align-items:center;gap:4px}
.school-name .dot{width:14px;height:14px;border-radius:50%;background:var(--yellow-bright)}
.band{position:absolute;left:0;top:101px;width:100%;height:29px;background:var(--yellow);color:var(--ink);font-weight:300;font-size:22px;line-height:29px;padding-left:24px}
.band--thin{height:9px}
.card{position:absolute;left:9px;width:456px;background:var(--panel);border-radius:7px;overflow:hidden}
.poster--steps .card{top:141px;height:519px}
.poster--ai .card{top:131px;height:507px}

/* steps poster */
.flow{position:absolute;left:0;top:15px;width:100%;height:24px}
.num{position:absolute;top:0;width:24px;height:24px;border-radius:50%;background:var(--navy);color:var(--yellow-bright);font-weight:800;font-size:16px;line-height:24px;text-align:center}
.arrow{position:absolute;top:6px;height:12px}
.visual{position:absolute;top:49px;height:90px;border-radius:8px}
.step-name{position:absolute;top:150px;width:136px;text-align:center;color:var(--navy);font-weight:900;font-size:19px;line-height:21px}
.box{position:absolute;top:202px;width:136px;height:202px;border:1.2px solid var(--navy);border-radius:6px;background:var(--soft);overflow:hidden}
.box-head{height:45px;background:var(--yellow);display:flex;align-items:center;justify-content:center;text-align:center;font-weight:700;font-size:12px;line-height:13px;color:var(--text);padding:0 4px}
.box ul{list-style:none;padding:8px 6px 0 12px}
.box li{position:relative;padding-left:11px;font-size:10.3px;line-height:14.5px;color:var(--text);margin-bottom:3.8px}
.box li::before{content:"";position:absolute;left:0;top:5px;width:4px;height:4px;border-radius:50%;background:var(--navy)}
.box .then{font-weight:600;font-size:10.3px;line-height:14.5px;color:var(--text);padding:0 6px 0 12px}
.motto{position:absolute;top:417px;width:136px;height:26px;border-radius:7px;background:var(--navy);color:#fff;font-weight:900;font-size:16px;line-height:26px;text-align:center}
.motto b{color:var(--yellow-bright);font-weight:900}
.col-1{left:15px}.col-2{left:161px}.col-3{left:306px}
.refs{position:absolute;left:0;bottom:0;width:100%;height:74px;background:var(--soft);padding:7px 27px 0;font-size:6.3px;line-height:8px;color:#444}
.refs h4{font-size:6.5px;font-weight:600;margin-bottom:1px}

/* ai poster */
.sec-title{position:absolute;left:0;width:100%;text-align:center;color:var(--navy);font-weight:800;font-size:19px;line-height:22px}
.musts{position:absolute;list-style:none}
.musts li{position:relative;padding-left:15px;font-weight:600;font-size:11.3px;line-height:13.8px;color:var(--text);margin-bottom:4px}
.musts li::before{content:"";position:absolute;left:0;top:3px;width:7px;height:7px;border:1px solid var(--navy)}
.musts li::after{content:"";position:absolute;left:2px;top:4px;width:3px;height:4px;border-right:1.2px solid var(--navy);border-bottom:1.2px solid var(--navy);transform:rotate(40deg)}
.ai-art{position:absolute;left:342px;top:28px;width:100px;height:106px;border-radius:10px;background:linear-gradient(135deg,#e4e7f4,#f7f2c4)}
.help{position:absolute;left:15px;top:143px;width:426px;height:197px;background:var(--yellow);border-radius:7px}
.help .sec-title{top:7px}
.help-sub{position:absolute;top:29px;width:100%;text-align:center;color:var(--navy);font-weight:300;font-size:12.5px}
.help-item{position:absolute;top:56px;width:106px;height:134px}
.help-item + .help-item{border-left:1px solid #8c8a5a}
.help-icon{position:absolute;left:26px;top:0;width:56px;height:66px}
.help-label{position:absolute;left:0;top:76px;width:100%;text-align:center;font-weight:600;font-size:11.3px;line-height:13px;color:var(--text)}
.cannot-title{top:353px}
.nots{position:absolute;top:380px;left:15px;width:426px;display:flex;gap:8px}
.not{width:101px;height:112px;border:1px solid var(--navy);border-radius:5px;background:var(--soft);text-align:center;padding-top:6px}
.not svg{display:block;margin:0 auto 7px}
.not p{font-weight:600;font-size:10.3px;line-height:11.8px;color:var(--text);padding:0 3px}
.footer-line{position:absolute;left:0;top:645px;width:100%;text-align:center;color:#fff;font-weight:600;font-size:11.5px}
</style>
</head>
<body>
<main class="canvas">

  <!-- Poster: before asking the teacher -->
  <section class="poster poster--steps">
    <header class="header">
      <h1 class="title">BEFORE YOU ASK<br><span class="accent">THE TEACHER...</span></h1>
      <div class="school-name"><span class="dot"></span>Tolvane SHS</div>
    </header>
    <div class="band">TRY THESE STEPS FIRST!</div>

    <div class="card">
      <div class="flow">
        <span class="num" style="left:71px">1</span>
        <svg class="arrow" style="left:103px;width:102px" viewBox="0 0 102 12"><line x1="0" y1="6" x2="96" y2="6" stroke="#2f3f96" stroke-width="1.2" stroke-dasharray="5 3"/><path d="M96 3 L100 6 L96 9" fill="none" stroke="#2f3f96" stroke-width="1.2"/></svg>
        <span class="num" style="left:217px">2</span>
        <svg class="arrow" style="left:250px;width:102px" viewBox="0 0 102 12"><line x1="0" y1="6" x2="96" y2="6" stroke="#2f3f96" stroke-width="1.2" stroke-dasharray="5 3"/><path d="M96 3 L100 6 L96 9" fill="none" stroke="#2f3f96" stroke-width="1.2"/></svg>
        <span class="num" style="left:363px">3</span>
      </div>

      <div class="visual" role="img" aria-label="Head outline with a glowing lightbulb, for thinking first" style="left:40px;width:86px;background:linear-gradient(135deg,#e1e5f3,#f8f1bd)"></div>
      <svg class="visual" style="left:195px;width:70px" viewBox="0 0 70 90" aria-hidden="true">
        <rect x="3" y="13" width="64" height="74" rx="7" fill="none" stroke="#2f3f96" stroke-width="4"/>
        <rect x="20" y="6" width="30" height="14" rx="4" fill="#fff" stroke="#2f3f96" stroke-width="4"/>
        <line x1="14" y1="35" x2="40" y2="35" stroke="#2f3f96" stroke-width="4" stroke-linecap="round"/>
        <line x1="14" y1="50" x2="40" y2="50" stroke="#2f3f96" stroke-width="4" stroke-linecap="round"/>
        <line x1="14" y1="65" x2="40" y2="65" stroke="#2f3f96" stroke-width="4" stroke-linecap="round"/>
        <path d="M46 35 l4 4 l7-8 M46 50 l4 4 l7-8 M46 65 l4 4 l7-8" fill="none" stroke="#f1d21c" stroke-width="3.5" stroke-linecap="round" stroke-linejoin="round"/>
      </svg>
      <div class="visual" role="img" aria-label="Three people with speech bubbles above them, for asking others" style="left:330px;width:95px;background:linear-gradient(135deg,#f8f1bd,#e1e5f3)"></div>

      <h2 class="step-name col-1">THINK<br>FIRST</h2>
      <h2 class="step-name col-2">CHECK YOUR<br>SUPPORTS</h2>
      <h2 class="step-name col-3">ASK 3<br>BEFORE ME</h2>

      <div class="box col-1">
        <div class="box-head">Don't give up<br>straight away.</div>
        <ul>
          <li>Read the question carefully.</li>
          <li>Identify what you already know.</li>
          <li>Try a strategy you've used before.</li>
          <li>Give yourself thinking time.</li>
        </ul>
      </div>
      <div class="box col-2">
        <div class="box-head">Before asking for<br>help, check:</div>
        <ul>
          <li>Learning goal and success criteria.</li>
          <li>Worked examples.</li>
          <li>Class notes.</li>
          <li>Classroom displays.</li>
          <li>Kluma resources.</li>
          <li>Task sheet and instructions.</li>
        </ul>
      </div>
      <div class="box col-3">
        <div class="box-head">Ask three sources before asking the teacher:</div>
        <ul>
          <li>A person (partner or neighbour)</li>
          <li>A place (notes, display, Kluma)</li>
          <li>A resource (worked example, task sheet)</li>
        </ul>
        <p class="then">Then ask the teacher if you still need help.</p>
      </div>

      <div class="motto col-1">WE <b>BELIEVE</b></div>
      <div class="motto col-2">WE <b>STRIVE</b></div>
      <div class="motto col-3">WE <b>ACHIEVE</b></div>

      <footer class="refs">
        <h4>References</h4>
        <p>Harwick, D. (2025). Why Students Don't Ask for Help – And How to Change That. Downloaded 24/04/2026 from: https://www.learnwell.org/article/students-asking-help/</p>
        <p>ERCA. (2024). Supporting Self-Regulated Learning. Downloaded 24/04/2026 from: https://www.evidencehub.edu.au/files/2024-02/supporting-self-regulated-learning.pdf</p>
      </footer>
    </div>
  </section>

  <!-- Poster: using AI responsibly -->
  <section class="poster poster--ai">
    <header class="header">
      <h1 class="title" style="left:22px">USING AI AND OTHER<br>TOOLS RESPONSIBLY</h1>
      <div class="school-name"><span class="dot"></span>Tolvane SHS</div>
    </header>
    <div class="band band--thin"></div>

    <div class="card">
      <h2 class="sec-title" style="top:9px">WHAT YOU MUST DO:</h2>
      <ul class="musts" style="left:22px;top:39px;width:175px">
        <li>Complete your own work</li>
        <li>Demonstrate your progress (drafts, notes, planning, revisions)</li>
        <li>Use feedback to improve your work</li>
      </ul>
      <ul class="musts" style="left:208px;top:39px;width:125px">
        <li>Demonstrate your understanding of the ideas in your submission</li>
      </ul>
      <div class="ai-art" role="img" aria-label="Brain outline joined to circuit lines around an AI chip"></div>

      <div class="help">
        <h2 class="sec-title">WHAT AI CAN HELP YOU DO</h2>
        <p class="help-sub">(when approved by your teacher)</p>

        <div class="help-item" style="left:0">
          <div class="help-icon" role="img" aria-label="Brain with sparks, for brainstorming" style="background:linear-gradient(135deg,#d9ddef,#eef0f8);border-radius:10px"></div>
          <p class="help-label">Brainstorm<br>ideas</p>
        </div>
        <div class="help-item" style="left:106px">
          <svg class="help-icon" viewBox="0 0 56 66" aria-hidden="true">
            <rect x="4" y="2" width="40" height="56" rx="3" fill="none" stroke="#2f3f96" stroke-width="3"/>
            <rect x="10" y="12" width="6" height="6" fill="none" stroke="#2f3f96" stroke-width="2"/>
            <rect x="10" y="26" width="6" height="6" fill="none" stroke="#2f3f96" stroke-width="2"/>
            <rect x="10" y="40" width="6" height="6" fill="none" stroke="#2f3f96" stroke-width="2"/>
            <line x1="20" y1="15" x2="36" y2="15" stroke="#2f3f96" stroke-width="2.5"/>
            <line x1="20" y1="29" x2="30" y2="29" stroke="#2f3f96" stroke-width="2.5"/>
            <circle cx="38" cy="41" r="10" fill="#f3ea7b" stroke="#fff" stroke-width="3"/>
            <path d="M33 41 l3 3 l6-6" fill="none" stroke="#fff" stroke-width="2.5"/>
            <line x1="45" y1="48" x2="53" y2="57" stroke="#fff" stroke-width="4" stroke-linecap="round"/>
          </svg>
          <p class="help-label">Check spelling,<br>grammar and<br>clarity</p>
        </div>
        <div class="help-item" style="left:213px">
          <div class="help-icon" role="img" aria-label="Phone with a speaking figure and sound wave, for text-to-speech" style="background:linear-gradient(135deg,#d9ddef,#eef0f8);border-radius:10px"></div>
          <p class="help-label">Read your work<br>aloud using<br>text-to-speech<br>tools</p>
        </div>
        <div class="help-item" style="left:319px">
          <svg class="help-icon" viewBox="0 0 66 66" style="left:18px;width:66px" aria-hidden="true">
            <rect x="8" y="52" width="6" height="12" fill="#2f3f96"/>
            <rect x="18" y="44" width="6" height="20" fill="#2f3f96"/>
            <rect x="28" y="36" width="6" height="28" fill="#2f3f96"/>
            <path d="M2 46 Q30 40 52 12" fill="none" stroke="#2f3f96" stroke-width="5" stroke-linecap="round"/>
            <path d="M44 10 L56 4 L55 18 Z" fill="#2f3f96"/>
            <circle cx="50" cy="46" r="10" fill="none" stroke="#fff" stroke-width="5" stroke-dasharray="4 3"/>
            <circle cx="50" cy="46" r="5" fill="#fff"/>
          </svg>
          <p class="help-label">Help identify<br>areas for<br>improvement<br>in a draft</p>
        </div>
      </div>

      <h2 class="sec-title cannot-title">WHAT YOU CANNOT DO:</h2>
      <div class="nots">
        <div class="not"><svg width="30" height="30" viewBox="0 0 30 30" aria-hidden="true"><circle cx="15" cy="15" r="12" fill="none" stroke="#d3292e" stroke-width="3"/><path d="M10 10 L20 20 M20 10 L10 20" stroke="#d3292e" stroke-width="3" stroke-linecap="round"/></svg><p>Submit AI-generated work as your own</p></div>
        <div class="not"><svg width="30" height="30" viewBox="0 0 30 30" aria-hidden="true"><circle cx="15" cy="15" r="12" fill="none" stroke="#d3292e" stroke-width="3"/><path d="M10 10 L20 20 M20 10 L10 20" stroke="#d3292e" stroke-width="3" stroke-linecap="round"/></svg><p>Copy and paste AI responses without acknowledging or adapting them</p></div>
        <div class="not"><svg width="30" height="30" viewBox="0 0 30 30" aria-hidden="true"><circle cx="15" cy="15" r="12" fill="none" stroke="#d3292e" stroke-width="3"/><path d="M10 10 L20 20 M20 10 L10 20" stroke="#d3292e" stroke-width="3" stroke-linecap="round"/></svg><p>Use AI tools to complete the whole task for you</p></div>
        <div class="not"><svg width="30" height="30" viewBox="0 0 30 30" aria-hidden="true"><circle cx="15" cy="15" r="12" fill="none" stroke="#d3292e" stroke-width="3"/><path d="M10 10 L20 20 M20 10 L10 20" stroke="#d3292e" stroke-width="3" stroke-linecap="round"/></svg><p>Submit work that does not demonstrate your understanding</p></div>
      </div>
    </div>

    <p class="footer-line">If you didn't create, develop and understand it, it isn't your work.</p>
  </section>

</main>
</body>
</html>
```